company profile catalogue for Architecture and Interior Design and project management company

We target private customers who want to design a villa or a residential palace. We also target international brands, restaurants, furniture stores and malls.

Our logo on the front page.
Simple but inviting and professional.
The goal is to convey to the customer that we are professional design professionals and professional contractors.
And accuracy in action.
And commitment to the duration of the project.

We are Architectural and Interior design firm and we want a company profile catalogue which has the following:

Three sections with a small difference in theme (in colors) which demo the following
(It contains a group of projects with photos with a description for each photo included) :
A- (Architectural design)
B- (Interior design)
C- (Contracting and Project management)

We want only (7) pages to be designed, which will contain the following:
1- Front Cover page
2- Back cover page
3- Introduction page (Text & 1 Picture)
4- Document page (contain also text w/o 1 picture)
5&6&7- Three pages (which will contain pictures for project and should be flexible, their scheme as following:)
• Contain 1 picture with text
• Contain 2 pictures with text
• Contain 3 pictures with text

Notes:
1- The catalog structure guide also included
2- We have attached our current profile so you can take an idea how the main structure of the catalog (87MB):
https://www.filecrate-example.net/s/qmra82pzk4lwtcn/k%26mprofile2017-rev1.1.pdf?dl=0
3- We also attached the logo of our firm

Target Market(s)

Industry/Entity Type

Architecture

Font styles to use
Serif

Requirements
Must have
• Our logo on the front page.
• Simple but inviting and professional.
• The goal is to convey to the customer that we are professional design professionals and professional contractors.
• And accuracy in action.
• And commitment to the duration of the project.
Nice to have
• Our logo and The distinctive colors of each department
Should not have
• Should not use anything from the previous design, we are looking for something new and elegant.

```html
<!DOCTYPE html>
<html lang="ar" dir="rtl">
<head>
<meta charset="utf-8">
<title>نبذة عن المؤسسة</title>
<link rel="stylesheet" href="https://fonts.googleapis.com/css2?family=Tajawal:wght@300;500;700;800&family=Open+Sans:wght@400&display=swap">
<style>
  :root {
    --brand-red: #d8062b;
    --brand-maroon: #6e0f1f;
    --slate: #3a414b;
    --body-grey: #5a5a5a;
    --page-bg: #ffffff;
    --folio-text: #b9bec5;
  }
  * { margin: 0; padding: 0; box-sizing: border-box; }
  html, body {
    width: 1200px;
    height: 846px;
    overflow: hidden;
    background: var(--page-bg);
  }
  .page {
    position: relative;
    width: 1200px;
    height: 846px;
    background: var(--page-bg);
    font-family: "Tajawal", sans-serif;
  }
  .pattern-field {
    position: absolute;
    left: 72px;
    top: 0;
    width: 730px;
    height: 432px;
  }
  .folio {
    position: absolute;
    left: 1029px;
    top: 0;
    width: 98px;
    height: 129px;
    background: var(--slate);
    color: var(--folio-text);
    font-family: "Open Sans", sans-serif;
    font-size: 24px;
    text-align: center;
    line-height: 1;
    padding-top: 66px;
    direction: ltr;
  }
  .section-title {
    position: absolute;
    right: 126px;
    top: 440px;
    text-align: right;
  }
  .section-title .kicker {
    display: block;
    color: var(--brand-red);
    font-weight: 300;
    font-size: 44px;
    line-height: 56px;
  }
  .section-title .main {
    display: block;
    color: var(--brand-maroon);
    font-weight: 800;
    font-size: 50px;
    line-height: 60px;
  }
  .intro-text {
    position: absolute;
    left: 72px;
    top: 446px;
    width: 730px;
    color: var(--body-grey);
    font-weight: 700;
    font-size: 16.5px;
    line-height: 34px;
    text-align: justify;
    text-align-last: right;
  }
  .intro-text p + p { margin-top: 32px; }
  .latin { font-family: "Tajawal", sans-serif; font-weight: 800; direction: ltr; unicode-bidi: isolate; font-size: 19px; }
</style>
</head>
<body>
<main class="page">
  <svg class="pattern-field" role="img" aria-label="Red geometric interlocking star pattern" viewBox="0 0 730 432" width="730" height="432">
    <rect width="730" height="432" fill="var(--brand-red)"/>
  </svg>

  <div class="folio">6</div>

  <h1 class="section-title">
    <span class="kicker">نبذة عن</span>
    <span class="main">المؤسسة</span>
  </h1>

  <section class="intro-text">
    <p>تأسست مؤسسة <span class="latin">K&amp;M</span> في مدينة الرياض مطلع الألفية الجديدة كمكتب هندسي يضع المخططات لأرقى المباني والقصور، منطلقة من فهم خاص لعالم الهندسة المعمارية وآخر ما توصلت إليه علوم التصميم والديكورات في العالم. وسرعان ما وسّعت المؤسسة نشاطاتها وأقسامها لتصبح مؤسسة شاملة، تعمل بدءاً من نقل الأفكار إلى الورق حتى الإشراف عليها وتنفيذها على أكمل وجه. وذلك انطلاقاً من فهمها العميق لمراحل العمل بدءاً من التصورات حتى نقله إلى حيز التنفيذ، خاصة وأنها من وضعت التفاصيل الأولى.</p>
    <p>ويدير مؤسسة <span class="latin">K&amp;M</span> اليوم فريق محترف من الإداريين والمهندسين كما يعمل في أقسامها أهم الفنيين والحرفيين ممن هم على درجة عالية من الكفاءة المهنية، كما تمتلك المؤسسة المعدات اللازمة لإدارة المشاريع والإشراف عليها.</p>
  </section>
</main>
</body>
</html>
```